College Admissions Consulting needs a small street facing sign for new office location.

I need a graphic design to be used inside window for a banner/sign in office location on a high walking traffic city street, for my company, Campus Lantern. I work with high school students and families on the college planning and selection application process. Please check out the website to learn more about what I do (www.mycampuslantern.example). The banner will be used to market our services at our office location. The final design should utilize logo colors, phone number, and website/email information. I'd like to incorporate a my picture in someway because of face recognition. To be printed on a posterboard or vinyl banner.

Target Market(s)

Parents of high school aged children.

Industry/Entity Type

Education

Font styles to use
Sans Serif

Colors
abd037

Requirements
Must have
• Clean, attractive, and professional design. Attract the attention of people walking by. Information must be clear and readable (phone/email, etc.).
Nice to have
• Utilize the picture with crossed arms (without the brown background on picture).
Emphasize tagline:
Mastering The College Admission Process
....with personalized, professional guidance in planning, selecting, and applying to the right colleges.

```html
<!DOCTYPE html>
<html lang="en">
<head>
<meta charset="utf-8">
<title>Campus Lantern – Window Banner</title>
<link rel="stylesheet" href="https://fonts.googleapis.com/css2?family=Montserrat:wght@300;400;600;700&family=Open+Sans:ital,wght@1,700&family=Roboto+Condensed:wght@700&display=swap">
<style>
  :root{
    --charcoal:#464648;
    --lime:#7dc231;
    --lime-light:#abd037;
    --lime-pale:#b5dc84;
    --ink:#38393a;
    --white:#ffffff;
    --page:#e6e6e6;
  }
  *{margin:0;padding:0;box-sizing:border-box}
  html,body{width:1200px;height:1200px;overflow:hidden;background:var(--page)}
  .banner{position:absolute;left:45px;top:239px;width:1109px;height:739px;background:var(--charcoal);overflow:hidden;font-family:"Montserrat",sans-serif}
  .header{position:absolute;left:0;top:0;width:100%;height:213px;background:var(--charcoal)}
  .brand-dot{position:absolute;left:46px;top:52px;width:100px;height:100px;border-radius:50%;background:var(--lime)}
  .brand-name{position:absolute;left:185px;top:48px;font-size:62px;font-weight:600;color:var(--white);line-height:1;white-space:nowrap}
  .brand-tagline{position:absolute;left:187px;top:139px;font-size:19px;font-weight:600;color:var(--white);letter-spacing:.5px;white-space:nowrap}
  .divider{position:absolute;left:0;top:213px;width:100%;height:5px;background:var(--lime)}
  .hero{position:absolute;left:0;top:226px;width:100%;height:379px;background:radial-gradient(circle at 690px 190px,var(--lime-pale) 0%,var(--lime-light) 30%,var(--lime) 70%)}
  .hero-rings{position:absolute;left:0;top:0}
  .headline{position:absolute;left:30px;width:708px;top:20px;text-align:center;color:var(--white);font-weight:700;font-size:46px;line-height:52px;letter-spacing:.3px}
  .headline-rule{position:absolute;left:113px;top:124px;width:536px;height:2px;background:var(--ink)}
  .subline{position:absolute;left:80px;width:608px;top:144px;text-align:center;color:var(--ink);font-family:"Open Sans",sans-serif;font-style:italic;font-weight:700;font-size:25px;line-height:31px;text-transform:uppercase;letter-spacing:-.3px}
  .cta{position:absolute;left:134px;top:242px;width:496px;height:123px;background:var(--charcoal);border:3px solid var(--lime);box-shadow:inset 0 0 0 2px #5a9a24;text-align:center;white-space:nowrap}
  .cta-label{display:block;margin-top:10px;font-size:30px;font-weight:300;color:var(--lime-light);letter-spacing:4px;line-height:40px}
  .cta-phone{display:block;font-family:"Roboto Condensed",sans-serif;font-weight:700;font-size:52px;line-height:60px;color:var(--white)}
  .portrait{position:absolute;left:710px;top:12px;width:344px;height:593px;border-radius:170px 170px 0 0;background:linear-gradient(180deg,#3b3230 0%,#2a2a2a 35%,#161616 100%)}
  .footer{position:absolute;left:0;top:605px;width:100%;height:134px;background:var(--charcoal)}
  .contact{position:absolute;left:47px;display:flex;align-items:center;gap:14px;color:var(--white);font-size:25px;font-weight:400;white-space:nowrap}
  .contact svg{width:22px;height:22px}
  .contact-email{top:24px}
  .contact-web{top:76px}
  .accent{color:var(--lime-light);font-weight:600}
  .footer-slash{position:absolute;left:0;top:0}
  .person-name{position:absolute;left:640px;width:444px;top:40px;text-align:center;font-size:48px;font-weight:700;color:var(--lime);letter-spacing:1px;white-space:nowrap}
</style>
</head>
<body>
<div class="banner">
  <header class="header">
    <span class="brand-dot"></span>
    <span class="brand-name">Campus Lantern</span>
    <span class="brand-tagline">MASTERING THE COLLEGE ADMISSION PROCESS</span>
  </header>
  <div class="divider"></div>

  <section class="hero">
    <svg class="hero-rings" width="1109" height="379" viewBox="0 0 1109 379">
      <circle cx="370" cy="70" r="185" fill="none" stroke="#8cc63f" stroke-opacity=".45" stroke-width="22"/>
      <circle cx="870" cy="60" r="150" fill="none" stroke="#7dc231" stroke-opacity=".55" stroke-width="22"/>
      <circle cx="740" cy="430" r="160" fill="none" stroke="#8cc63f" stroke-opacity=".4" stroke-width="20"/>
    </svg>
    <h1 class="headline">MASTERING THE COLLEGE<br>ADMISSION PROCESS</h1>
    <div class="headline-rule"></div>
    <p class="subline">With personalized, professional<br>guidance in planning, selecting,<br>and applying to the right colleges.</p>
    <div class="cta">
      <span class="cta-label">FREE CONSULTATION</span>
      <span class="cta-phone">555-310-GRAD (4723)</span>
    </div>
  </section>

  <div class="portrait" role="img" aria-label="Photo of the consultant, Mara Linden, smiling with arms crossed, wearing a black top"></div>

  <footer class="footer">
    <div class="contact contact-email">
      <svg viewBox="0 0 24 24" aria-hidden="true"><rect x="2" y="6" width="20" height="14" fill="none" stroke="#7dc231" stroke-width="2"/><path d="M2 6l10 8 10-8" fill="none" stroke="#7dc231" stroke-width="2"/></svg>
      <span>mara@mycampuslantern.example</span>
    </div>
    <div class="contact contact-web">
      <svg viewBox="0 0 24 24" aria-hidden="true"><circle cx="12" cy="12" r="10" fill="none" stroke="#7dc231" stroke-width="2"/><ellipse cx="12" cy="12" rx="4.5" ry="10" fill="none" stroke="#7dc231" stroke-width="1.6"/><path d="M2 12h20M4 7h16M4 17h16" stroke="#7dc231" stroke-width="1.6"/></svg>
      <span>www.<span class="accent">mycampuslantern</span>.example</span>
    </div>
    <svg class="footer-slash" width="1109" height="134" viewBox="0 0 1109 134"><line x1="623" y1="0" x2="552" y2="134" stroke="#ffffff" stroke-width="3"/></svg>
    <div class="person-name">MARA LINDEN</div>
  </footer>
</div>
</body>
</html>
```